Fancy&Artistic design bussiness card!

I want a business card for myself.I'm a cinephile.Love watching SF(especially distopia one),Cult(mostly from midnight movies),Chivalrous story film. My favorite film for example,○Lantern Ward (directed by morris Pellacott)○gaslights○owl of marrows○rusty lantern alley(Japanese film)○copper harbor○tinvelt ○warden of lanterns ○SOVEL○the harvest of the hollow moon ○El topoAnd I also love modern art. I love their way of using colors(Brent Mavolle,Lyle Dobrent, Calvabrini,etc..)I want to get a business card which is full of creativity, uniqueness and humor(related to movie or art would be much better).I will be very pleased if you would meet my expectations. Thank you.
Industry/Entity Type
Movie
Contact Information for Business Card
Name: HIROKAZU ENOMOTOAddress: 514 E62nd Avenue #2718 NewYork,NY 10024e-mail: Takuyashi@plumvane.com

```html
<!DOCTYPE html>
<html lang="en">
<head>
<meta charset="utf-8">
<title>Business Card – Takumaro Yashibe</title>
<link href="https://fonts.googleapis.com/css2?family=Ubuntu:wght@300;400;500;700&display=swap" rel="stylesheet">
<style>
  :root {
    --stage: #1b1b1b;
    --card-black: #060606;
    --card-charcoal: #2c2c2c;
    --card-graphite: #3a3a3a;
    --stripe-grey: #4a4a4a;
    --crimson: #c8133a;
    --crimson-soft: #b61f45;
    --text-white: #ffffff;
    --text-soft: #e6e6e6;
  }
  * { margin: 0; padding: 0; box-sizing: border-box; }
  html, body {
    width: 1200px; height: 1000px; overflow: hidden;
    background: var(--stage);
    font-family: "Ubuntu", sans-serif;
  }
  .canvas { position: relative; width: 1200px; height: 1000px; }

  .card {
    position: absolute;
    width: 700px; height: 400px;
    overflow: hidden;
    box-shadow: 0 18px 40px rgba(0,0,0,.6);
  }
  .card svg.card-art { position: absolute; inset: 0; }

  /* Back of card */
  .card-back { left: 420px; top: 70px; }
  .card-back .brand { position: absolute; left: 0; right: 0; top: 160px; text-align: center; }

  /* Front of card */
  .card-front { left: 80px; top: 520px; }
  .card-front .brand { position: absolute; left: 40px; width: 300px; top: 150px; text-align: center; }

  .brand-name { color: var(--text-white); font-size: 23px; line-height: 1.1; }
  .brand-name .light { font-weight: 300; }
  .brand-name .bold { font-weight: 700; }
  .brand-tagline {
    color: var(--text-soft); font-size: 12px; font-weight: 400;
    letter-spacing: .3px; margin-top: 4px;
  }

  .person { position: absolute; right: 42px; top: 38px; text-align: right; }
  .person-name {
    color: var(--text-white); font-size: 22px; font-weight: 500;
    letter-spacing: 1px;
  }
  .person-title {
    color: var(--text-soft); font-size: 15px; font-weight: 400;
    letter-spacing: .8px; margin-top: 4px; margin-right: 18px;
  }

  .contact { position: absolute; right: 40px; color: var(--text-white); text-align: right; font-size: 17px; }
  .contact-address { top: 262px; line-height: 1.3; }
  .contact-email { top: 347px; }
</style>
</head>
<body>
<main class="canvas">

  <section class="card card-back" aria-label="Business card back">
    <svg class="card-art" width="700" height="400" viewBox="0 0 700 400" aria-hidden="true">
      <defs>
        <linearGradient id="backGradient" x1="0" y1="0" x2="1" y2="1">
          <stop offset="0" stop-color="#0a0a0a"/>
          <stop offset="0.55" stop-color="#262626"/>
          <stop offset="1" stop-color="#3a3a3a"/>
        </linearGradient>
      </defs>
      <rect width="700" height="400" fill="url(#backGradient)"/>
      <rect class="accent-square" x="575" y="305" width="52" height="52" fill="#333" stroke="var(--crimson)" stroke-width="2.5"/>
      <polygon class="accent-triangle" points="648,345 662,345 662,331" fill="var(--crimson)"/>
    </svg>
    <div class="brand">
      <p class="brand-name"><span class="light">Your</span> <span class="bold">Company Name</span></p>
      <p class="brand-tagline">TAGLINE GOES HERE</p>
    </div>
  </section>

  <section class="card card-front" aria-label="Business card front">
    <svg class="card-art" width="700" height="400" viewBox="0 0 700 400" aria-hidden="true">
      <defs>
        <linearGradient id="panelGradient" x1="0" y1="0" x2="1" y2="1">
          <stop offset="0" stop-color="#1e1e1e"/>
          <stop offset="1" stop-color="#3a3a3a"/>
        </linearGradient>
        <clipPath id="panelClip">
          <polygon points="392,0 700,0 700,400 292,400"/>
        </clipPath>
      </defs>
      <rect width="700" height="400" fill="var(--card-black)"/>
      <g clip-path="url(#panelClip)">
        <rect width="700" height="400" fill="url(#panelGradient)"/>
        <rect class="band-address" x="0" y="250" width="700" height="68" fill="var(--crimson)"/>
        <rect class="band-divider" x="0" y="318" width="700" height="12" fill="var(--stripe-grey)"/>
        <rect class="band-email" x="0" y="330" width="700" height="58" fill="var(--crimson-soft)"/>
        <rect class="band-foot" x="0" y="388" width="700" height="12" fill="var(--stripe-grey)"/>
      </g>
    </svg>
    <div class="brand">
      <p class="brand-name"><span class="light">Your</span> <span class="bold">Company Name</span></p>
      <p class="brand-tagline">TAGLINE GOES HERE</p>
    </div>
    <div class="person">
      <p class="person-name">TAKUMARO YASHIBE</p>
      <p class="person-title">DESIGNATION</p>
    </div>
    <p class="contact contact-address">514 E62nd Avenue #2718 NewYork<br>NY 10391</p>
    <p class="contact contact-email">Takuyashi@plumvane.com</p>
  </section>

</main>
</body>
</html>
```